Lens Deal Ranger

This website is a price comparison site specialising in Digital Photographic equipment - DSLR Cameras & Lenses etc. It is going to operate along the lines of a site called www.shuttertallyhub.example
It must look much more professional and less home made than the afforementioned site. My site will be a direct competitor to shuttertallyhub, so it must look and operate much better.
The new site is first and foremost a price information site - it is not selling anything! The message it should send to visitors is one of impartiality and unbiased information, the shops it links to are the ones who will be selling products. People who visit this site, have already decided which product they are going to buy, they are now at the stage of looking for which shop is offering the best deal based on PRICE. This is NOT a "WHAT CAMERA" site. This site is comparing DIFFERENT PRICES for the same product offered by a list of SHOPS. The site should look expensive. I have a couple of Logos which you can look at for colour ideas. I like Blue, Silver, aluminium, stainless steel, White, Grey and Black. There must be lots of product category buttons to chose from. If you can come up with anything imaginative, I will appreciate any clever ideas. Some flash technology might be nice or something visually interesting happening to catch the visitors attention. There are lots of stock photos available on the net of the kind of products we will be dealing with. In particular VORTELL and KASURO Digital SLR Cameras and Lenses. All the other brands are definately second division. There will be no telephone number on the page. My Logo will be at the top of the page. I have uploaded two logos for you to take your pick and a very nice picture of a very expensivr DSLR camera which you might want to utilize.

Target Market(s)

Buyers of DSLR Camera equipment 70% Male, Age group 35 to 70. The products being compared on this site are all high ticket items. Customers are usually quite well off.

Industry/Entity Type

Camera

Requirements
Must have
• Must be simple and easy to navigate to find the desired product very easily.
Nice to have
• Should have a space on the front page for "TODAYS PRICE DROPS"

```html
<!DOCTYPE html>
<html lang="en">
<head>
<meta charset="utf-8">
<title>Lens Deal Ranger</title>
<link href="https://fonts.googleapis.com/css2?family=Oswald:wght@300;400&family=PT+Sans:ital,wght@0,400;0,700;1,400&family=Bree+Serif&family=Ubuntu:wght@400;700&display=swap" rel="stylesheet">
<style>
:root{
  --black:#0d0d0d;
  --header-top:#3a3a3a;
  --header-bottom:#111;
  --accent:#0b66c2;
  --accent-dark:#0a3e80;
  --price-blue:#114a85;
  --link-blue:#1b5fb0;
  --grey-text:#666;
  --light-grey:#d9d9d9;
  --track:#e2e2e2;
  --white:#fff;
  --ink:#222;
}
*{margin:0;padding:0;box-sizing:border-box}
html,body{width:998px;height:1200px;overflow:hidden;background:var(--white)}
body{position:relative;font-family:"Ubuntu",sans-serif;color:var(--ink)}
.abs{position:absolute}

.topbar{left:0;top:0;width:998px;height:36px;background:var(--black)}
.login{left:112px;top:17px;font:11px "PT Sans",sans-serif;color:#ddd}
.nav{left:748px;top:0;height:36px;display:flex;align-items:flex-end;font:11px "PT Sans",sans-serif;color:#ccc}
.nav span{padding:0 5px 4px}
.nav .active{background:#555;height:36px;display:flex;align-items:flex-end;padding:0 3px 4px}

.header{left:0;top:36px;width:998px;height:317px;background:linear-gradient(#3c3c3c,#262626 45%,#0f0f0f);border-bottom:3px solid var(--accent)}
.brand-mark{left:96px;top:40px;width:104px;height:104px;border-radius:50%;background:#c9ccd1;border:5px solid #eef0f2}
.brand-name{left:230px;top:64px;font:300 40px "Oswald",sans-serif;color:#e6e6e6;letter-spacing:1px}
.drops-shadow{left:640px;top:100px;width:280px;height:24px;border-radius:50%;background:radial-gradient(rgba(0,0,0,.85),transparent 70%)}
.drops{left:697px;top:56px;width:172px;height:62px;background:linear-gradient(#1e7fe0,#0a4fa8);border:1px solid #2a8af0;color:#fff;font:19px/24px "Bree Serif",serif;text-align:center;padding-top:7px;text-shadow:0 1px 2px #000}

.slider{left:131px;top:156px;width:732px;height:199px;background:linear-gradient(#fafafa,#dcdcdc);border-radius:6px;box-shadow:0 10px 12px -6px rgba(0,0,0,.5)}
.slide{left:145px;top:170px;width:704px;height:170px;border-radius:6px;background:linear-gradient(#fff,#eee 45%,#e0e0e0 55%,#fafafa);border:1px solid #d0d0d0}
.steps-num{left:165px;top:186px;font:400 120px/1 "Oswald",sans-serif;color:#1a5a9a}
.steps-word{left:255px;top:218px;font:400 52px/1 "PT Sans",sans-serif;color:#2b8ee0;letter-spacing:1px}
.badge{left:620px;top:210px;width:198px;height:110px;background:linear-gradient(#2f6fba,#173f7a);border-radius:4px 4px 40px 40px;border:2px solid #5a8fd0;color:#fff;font:30px/34px "Bree Serif",serif;text-align:center;padding-top:16px;transform:rotate(-2deg)}
.dots{left:804px;top:330px;display:flex;gap:3px}
.dots i{width:6px;height:6px;border-radius:50%;background:#777;display:block}
.dots i:first-child{background:var(--accent)}

.welcome{left:0;top:376px;width:998px;text-align:center;font:400 24px "PT Sans",sans-serif;color:var(--grey-text);text-shadow:0 1px 0 #fff,0 1px 2px #aaa}
.note{left:96px;top:414px;font:italic 11px "PT Sans",sans-serif;color:#333}

.step-label{top:450px;font:12px "PT Sans",sans-serif;color:#777}
.track{left:97px;top:488px;width:803px;height:14px;background:var(--track);border:1px solid #c8c8c8;border-radius:4px}
.step-dot{width:46px;height:46px;border-radius:50%;background:linear-gradient(#cfcfcf,#7a7a7a);border:4px solid #eee;box-shadow:0 1px 3px rgba(0,0,0,.4);color:#fff;font:700 24px/38px "PT Sans",sans-serif;text-align:center;top:472px}
.done{top:526px;font:12px "PT Sans",sans-serif;color:var(--link-blue)}

.picker{top:566px;width:233px;height:36px;background:linear-gradient(#aaa,#777);border-radius:3px;border-bottom:2px solid #555;color:#fff}
.picker .num{position:absolute;left:13px;top:0;font:700 30px/36px "PT Sans",sans-serif}
.picker svg.chev{position:absolute;left:38px;top:0}
.picker .val{position:absolute;left:50px;right:40px;top:0;text-align:center;font:700 13px/36px "Ubuntu",sans-serif}
.picker svg.down{position:absolute;right:10px;top:9px}

.col-head{top:653px;font:13px "Ubuntu",sans-serif}
.dots-line{left:96px;width:806px;border-top:1px dotted #777}

.row{left:96px;width:806px;height:102px}
.retailer{position:absolute;left:12px;top:8px;font:700 17px "Ubuntu",sans-serif;color:#222}
.retailer-sub{position:absolute;left:27px;top:36px;font:13px "Ubuntu",sans-serif}
.extras{position:absolute;left:219px;top:13px;font:13px "Ubuntu",sans-serif}
.price{position:absolute;left:410px;top:0;width:121px;text-align:right;font:14px/20px "Ubuntu",sans-serif}
.price .deliv{border-bottom:1px solid #444;display:flex;justify-content:space-between;padding-left:6px}
.price .total{font:700 18px/26px "Ubuntu",sans-serif;color:var(--price-blue)}
.shop-btn{position:absolute;left:696px;top:6px;width:101px;height:29px;background:linear-gradient(#1e6bc0,#0a3d80);color:#fff;font:18px/29px "Bree Serif",serif;text-align:center;text-shadow:0 1px 1px #000}

.footer{left:0;top:1115px;width:998px;height:85px;background:linear-gradient(#fafafa,#e8e8e8 60%,#dedede)}
.footer-mark{left:465px;top:1126px;width:40px;height:40px;border-radius:50%;background:#8a8a8a}
.copyright{left:0;top:1177px;width:998px;text-align:center;font:11px "Ubuntu",sans-serif;color:#111}
</style>
</head>
<body>
<div class="abs topbar"></div>
<div class="abs login">login / register</div>
<nav class="abs nav"><span class="active">Home</span>|<span>About us</span>|<span>Contact</span></nav>

<header class="abs header"></header>
<div class="abs brand-mark" aria-hidden="true"></div>
<div class="abs brand-name">LENS DEAL RANGER</div>
<div class="abs drops-shadow"></div>
<div class="abs drops">Today’s<br>Price Drops</div>

<div class="abs slider"></div>
<div class="abs slide"></div>
<div class="abs steps-num">3</div>
<div class="abs steps-word">STEPS</div>
<svg class="abs" style="left:450px;top:246px" width="120" height="14" viewBox="0 0 120 14" aria-hidden="true">
  <g fill="#8a8a8a"><path d="M2 2l12 5-12 5z"/><path d="M36 2l12 5-12 5z"/><path d="M70 2l12 5-12 5z"/><path d="M104 2l12 5-12 5z"/></g>
</svg>
<div class="abs badge">BEST<br>PRICE!</div>
<div class="abs dots"><i></i><i></i><i></i><i></i></div>

<h1 class="abs welcome">Welcome to Lens Deal Ranger!</h1>
<p class="abs note">*Please follow these steps to get the best prices:</p>

<div class="abs step-label" style="left:106px">Step 1 - Select a Category</div>
<div class="abs step-label" style="left:428px">Step 2 - Select a Producer</div>
<div class="abs step-label" style="left:767px">Step 3 - Select a Model</div>
<div class="abs track"></div>
<div class="abs step-dot" style="left:151px">1</div>
<div class="abs step-dot" style="left:470px">2</div>
<div class="abs step-dot" style="left:799px">3</div>
<div class="abs done" style="left:160px">Done</div>
<div class="abs done" style="left:479px">Done</div>
<div class="abs done" style="left:811px">Done</div>

<div class="abs picker" style="left:91px"><span class="num">1</span><svg class="chev" width="12" height="36" viewBox="0 0 12 36"><path d="M1 0l9 18-9 18" fill="none" stroke="#ddd" stroke-width="2"/></svg><span class="val">DSLRs</span><svg class="down" width="16" height="18" viewBox="0 0 16 18"><path d="M1 1l7 7 7-7M1 9l7 7 7-7" fill="none" stroke="#fff" stroke-width="3"/></svg></div>
<div class="abs picker" style="left:383px"><span class="num">2</span><svg class="chev" width="12" height="36" viewBox="0 0 12 36"><path d="M1 0l9 18-9 18" fill="none" stroke="#ddd" stroke-width="2"/></svg><span class="val">KASURO</span><svg class="down" width="16" height="18" viewBox="0 0 16 18"><path d="M1 1l7 7 7-7M1 9l7 7 7-7" fill="none" stroke="#fff" stroke-width="3"/></svg></div>
<div class="abs picker" style="left:670px"><span class="num">3</span><svg class="chev" width="12" height="36" viewBox="0 0 12 36"><path d="M1 0l9 18-9 18" fill="none" stroke="#ddd" stroke-width="2"/></svg><span class="val">K7150</span><svg class="down" width="16" height="18" viewBox="0 0 16 18"><path d="M1 1l7 7 7-7M1 9l7 7 7-7" fill="none" stroke="#fff" stroke-width="3"/></svg></div>

<div class="abs col-head" style="left:109px">Retailer</div>
<div class="abs col-head" style="left:358px">Extras</div>
<div class="abs col-head" style="left:566px">Price</div>
<div class="abs dots-line" style="top:672px"></div>

<div class="abs row" style="top:683px">
  <div class="retailer">brightmart</div><div class="retailer-sub">Brightmart</div>
  <div class="extras">FREE 8Gb Memory card</div>
  <div class="price"><div>200$</div><div class="deliv"><span>+</span><span>Delivery: 0.00$</span></div><div class="total">200$</div></div>
  <div class="shop-btn">View Shop</div>
</div>
<div class="abs dots-line" style="top:763px"></div>

<div class="abs row" style="top:785px">
  <div class="retailer">brightmart</div><div class="retailer-sub">Brightmart</div>
  <div class="extras">FREE 8Gb Memory card</div>
  <div class="price"><div>200$</div><div class="deliv"><span>+</span><span>Delivery: 0.00$</span></div><div class="total">200$</div></div>
  <div class="shop-btn">View Shop</div>
</div>
<div class="abs dots-line" style="top:865px"></div>

<div class="abs row" style="top:878px">
  <div class="retailer">brightmart</div><div class="retailer-sub">Brightmart</div>
  <div class="extras">FREE 8Gb Memory card</div>
  <div class="price"><div>200$</div><div class="deliv"><span>+</span><span>Delivery: 0.00$</span></div><div class="total">200$</div></div>
  <div class="shop-btn">View Shop</div>
</div>
<div class="abs dots-line" style="top:958px"></div>

<div class="abs row" style="top:980px">
  <div class="retailer">brightmart</div><div class="retailer-sub">Brightmart</div>
  <div class="extras">FREE 8Gb Memory card</div>
  <div class="price"><div>200$</div><div class="deliv"><span>+</span><span>Delivery: 0.00$</span></div><div class="total">200$</div></div>
  <div class="shop-btn">View Shop</div>
</div>
<div class="abs dots-line" style="top:1060px"></div>

<footer class="abs footer"></footer>
<div class="abs footer-mark" aria-hidden="true"></div>
<div class="abs copyright">© Lens Deal Ranger</div>
</body>
</html>
```